Quillmoor Properties, LLC. What we do is rehab homes for the purpose of flipping them and also have a rental portfolio as well.

We do not have a logo so that will need to be part of the design process

Would like, if possible to have a house or something with housing or remodeling incorporated in design.

Rental

Dale Wemberton
514 fenwick Ct.
Bartlett, il 60103
847-555-0142
Fax 630-555-0187

```html
<!DOCTYPE html>
<html lang="en">
<head>
<meta charset="utf-8">
<title>Quillmoor Properties – Business Card</title>
<link href="https://fonts.googleapis.com/css2?family=Open+Sans:wght@400;600&family=Ubuntu:wght@500&display=swap" rel="stylesheet">
<style>
  :root {
    --backdrop: #d9dcda;
    --card: #ffffff;
    --brand-blue: #1d4f8c;
    --ink: #2b2b2b;
    --ink-soft: #4a4a4a;
  }
  html, body {
    margin: 0;
    width: 1200px;
    height: 900px;
    overflow: hidden;
    background: var(--backdrop);
  }
  .card {
    position: absolute;
    left: 180px;
    top: 210px;
    width: 840px;
    height: 480px;
    background: var(--card);
    box-shadow: 0 6px 18px rgba(0,0,0,0.18);
    overflow: hidden;
    font-family: "Open Sans", sans-serif;
  }
  .brand {
    position: absolute;
    left: 60px;
    top: 196px;
    display: flex;
    align-items: center;
    gap: 14px;
  }
  .brand-square {
    width: 26px;
    height: 26px;
    background: var(--brand-blue);
  }
  .brand-name {
    font-family: "Ubuntu", sans-serif;
    font-weight: 500;
    font-size: 38px;
    line-height: 1.02;
    color: var(--brand-blue);
  }
  .accent-shape {
    position: absolute;
    left: 0;
    top: 0;
  }
  .person {
    position: absolute;
    right: 70px;
    top: 92px;
    text-align: right;
  }
  .person-name {
    font-size: 40px;
    color: var(--ink);
    line-height: 1;
  }
  .person-role {
    font-size: 13px;
    color: var(--ink-soft);
    margin-top: 4px;
  }
  .contacts {
    position: absolute;
    left: 580px;
    top: 250px;
    list-style: none;
    margin: 0;
    padding: 0;
    font-size: 15px;
    color: var(--ink-soft);
  }
  .contacts li {
    display: flex;
    align-items: center;
    gap: 10px;
    margin-bottom: 6px;
  }
  .contacts svg { width: 12px; height: 12px; fill: var(--ink); }
</style>
</head>
<body>
  <div class="card">
    <svg class="accent-shape" width="840" height="480" viewBox="0 0 840 480" aria-hidden="true">
      <polygon points="355,270 368,480 555,480" fill="var(--brand-blue)"/>
    </svg>

    <div class="brand">
      <div class="brand-square"></div>
      <div class="brand-name">Quillmoor<br>Properties</div>
    </div>

    <div class="person">
      <div class="person-name">Dale Wemberton</div>
      <div class="person-role">general manager</div>
    </div>

    <ul class="contacts">
      <li>
        <svg viewBox="0 0 24 24"><path d="M6.6 10.8a15.1 15.1 0 0 0 6.6 6.6l2.2-2.2c.3-.3.7-.4 1-.2 1.1.4 2.3.6 3.6.6.6 0 1 .4 1 1V20c0 .6-.4 1-1 1A17 17 0 0 1 3 4c0-.6.4-1 1-1h3.5c.6 0 1 .4 1 1 0 1.3.2 2.5.6 3.6.1.3 0 .7-.2 1z"/></svg>
        847-555-0142
      </li>
      <li>
        <svg viewBox="0 0 24 24"><path d="M6 2h10v6H6zM3 9h18v10H3zM6 14h4v2H6zM13 12h2v2h-2zM16 12h2v2h-2zM13 15h2v2h-2zM16 15h2v2h-2z"/></svg>
        630-555-0187
      </li>
      <li>
        <svg viewBox="0 0 24 24"><path d="M12 2a7 7 0 0 0-7 7c0 5.2 7 13 7 13s7-7.8 7-13a7 7 0 0 0-7-7zm0 9.5A2.5 2.5 0 1 1 12 6.5a2.5 2.5 0 0 1 0 5z"/></svg>
        514 fenwick Ct. Bartlett, il 60103
      </li>
    </ul>
  </div>
</body>
</html>
```